Bifold for voip company

Bifold for cloud voip company

Target Market(s)

Business owners

Industry/Entity Type

Software Developer

Colors

Designer to choose colors to be used in the design.

Requirements
Must have
• Modern clean design,
• will provide content to design winner

```html
<!DOCTYPE html>
<html lang="en">
<head>
<meta charset="utf-8">
<title>Nimbrix Bifold</title>
<link href="https://fonts.googleapis.com/css2?family=Montserrat:wght@300;400;500;600;700;800;900&display=swap" rel="stylesheet">
<style>
:root{
  --bg:#3e3e3e;
  --paper:#f4f4f5;
  --paper-shade:#e3e3e6;
  --purple:#4a2a7c;
  --purple-soft:#674489;
  --teal:#2bb0d4;
  --ink:#2f2f35;
  --muted:#6c6c74;
  --line:#d2d2d8;
  --photo-a:#1d2b3a;
  --photo-b:#5d7d92;
  --photo-c:#3fc4dc;
}
*{margin:0;padding:0;box-sizing:border-box}
html,body{width:1200px;height:824px;overflow:hidden;background:var(--bg);font-family:"Montserrat",sans-serif;color:var(--ink)}
.spread{position:absolute;left:40px;top:40px;width:1120px;height:744px;background:var(--paper);overflow:hidden}
.spine{position:absolute;left:559px;top:0;width:2px;height:100%;background:linear-gradient(var(--paper-shade),#d6d6da,var(--paper-shade))}
.deco{position:absolute;left:0;top:0}
.section-title{font-size:15px;font-weight:400;color:var(--ink);letter-spacing:.3px}
.section-title b{font-weight:700;color:var(--purple)}
.section-title::after{content:"";display:block;width:22px;height:2px;background:var(--teal);margin-top:5px}
.partners{position:absolute;left:60px;top:150px}
.partner-grid{display:grid;grid-template-columns:130px 130px;gap:10px 16px;margin-top:14px}
.partner{height:40px;background:#fff;border:1px solid var(--line);box-shadow:0 1px 3px rgba(0,0,0,.12);display:flex;align-items:center;justify-content:center;gap:7px;font-size:16px;font-weight:600;color:var(--purple)}
.partner i{width:10px;height:10px;background:var(--teal);border-radius:50%}
.clients{position:absolute;left:60px;top:370px}
.client-row{display:flex;gap:12px;margin-top:16px}
.client-row.second{margin-left:22px;margin-top:8px}
.client{width:50px;height:50px;border-radius:50%;background:#fff;box-shadow:0 1px 4px rgba(0,0,0,.18)}
.address{position:absolute;left:300px;top:540px;width:190px}
.dept{font-size:10.5px;font-weight:700;color:var(--purple);margin-top:14px;letter-spacing:.3px}
.addr{display:flex;gap:6px;font-size:9px;color:var(--muted);line-height:1.35;margin-top:4px}
.addr svg,.contact svg,.web svg{flex:none;margin-top:1px}
.web{display:flex;align-items:center;gap:6px;font-size:12px;color:var(--ink)}
.web b{color:var(--purple);font-weight:700}
.address .web{margin-top:18px}
.contacts{position:absolute;left:462px;top:548px;width:96px}
.contact{display:flex;gap:5px;font-size:8.5px;color:var(--muted);margin-bottom:5px;line-height:1.3}
.open{font-size:15px;font-weight:800;color:var(--ink);margin-top:8px;line-height:1}
.open span{color:var(--purple)}
.open small{display:block;font-size:7px;font-weight:600;margin-top:2px;letter-spacing:.2px}
.rule{position:absolute;height:1px;background:var(--purple-soft)}
.rule::before{content:"";position:absolute;left:-3px;top:-2px;width:5px;height:5px;border-radius:50%;background:var(--purple)}
.brand{position:absolute;right:60px;top:70px;display:flex;align-items:center;gap:10px;font-size:26px;font-weight:700;letter-spacing:2px;color:var(--purple)}
.brand i{width:26px;height:26px;background:var(--purple)}
.headline{position:absolute;right:50px;top:430px;text-align:right;color:var(--purple)}
.headline .light{font-size:26px;font-weight:300;color:var(--ink);letter-spacing:.5px}
.headline .big{font-size:48px;font-weight:900;line-height:1}
.headline .mid{font-size:30px;font-weight:800;line-height:1.1;letter-spacing:.5px}
.headline .bar{width:40px;height:3px;background:var(--purple);margin:6px 0 8px auto}
.tagline{font-size:16px;color:var(--ink);font-weight:400;line-height:1.35}
.tagline b{color:var(--teal);font-weight:700}
.right-web{position:absolute;left:600px;top:688px}
</style>
</head>
<body>
<div class="spread">
  <svg class="deco" width="1120" height="744" viewBox="0 0 1120 744">
    <defs>
      <linearGradient id="photoFill" x1="0" y1="0" x2="1" y2="1">
        <stop offset="0" stop-color="var(--photo-c)"/>
        <stop offset=".35" stop-color="var(--photo-b)"/>
        <stop offset="1" stop-color="var(--photo-a)"/>
      </linearGradient>
    </defs>
    <path d="M300 0 H640 L520 120 Q500 140 470 130 L300 60 Z" fill="var(--paper-shade)"/>
    <path d="M0 560 L170 600 Q200 610 190 640 L140 744 H0 Z" fill="var(--purple-soft)"/>
    <rect x="460" y="150" width="360" height="360" rx="46" transform="rotate(45 640 330)" fill="url(#photoFill)" role="img" aria-label="Photo of a businessman holding a tablet with a glowing cloud network diagram in front of a server room"/>
  </svg>
  <div class="spine"></div>

  <section class="partners">
    <h2 class="section-title">OUR <b>PARTNERS</b></h2>
    <div class="partner-grid">
      <div class="partner"><i></i>Arcline</div>
      <div class="partner"><i></i>streamwave</div>
      <div class="partner"><i></i>tallyo</div>
      <div class="partner"><i></i>ledgerly</div>
      <div class="partner"><i></i>Vocalis</div>
    </div>
  </section>

  <section class="clients">
    <h2 class="section-title">OUR <b>CLIENTS</b></h2>
    <div class="client-row"><div class="client"></div><div class="client"></div><div class="client"></div><div class="client"></div></div>
    <div class="client-row second"><div class="client"></div><div class="client"></div><div class="client"></div></div>
  </section>

  <section class="address">
    <h2 class="section-title">OUR <b>ADDRESS</b></h2>
    <p class="dept">TECHNICAL SERVICES :</p>
    <p class="addr"><svg width="8" height="10" viewBox="0 0 8 10"><path d="M4 0a4 4 0 0 1 4 4c0 3-4 6-4 6S0 7 0 4a4 4 0 0 1 4-4z" fill="var(--teal)"/></svg>480 Harbor Way Bldg C,<br>Suite 12 Lakeview, NJ 07000</p>
    <p class="dept">BILLING DEPARTMENT :</p>
    <p class="addr"><svg width="8" height="10" viewBox="0 0 8 10"><path d="M4 0a4 4 0 0 1 4 4c0 3-4 6-4 6S0 7 0 4a4 4 0 0 1 4-4z" fill="var(--teal)"/></svg>2150 Palm Crest Ave N. Bayside,<br>FL 33700</p>
    <p class="web"><svg width="11" height="11" viewBox="0 0 12 12"><circle cx="6" cy="6" r="5" fill="none" stroke="var(--teal)" stroke-width="1.2"/><path d="M1 6h10M6 1c2 2 2 8 0 10M6 1c-2 2-2 8 0 10" fill="none" stroke="var(--teal)"/></svg>www.<b>nimbrix</b>.com</p>
  </section>

  <section class="contacts">
    <p class="contact"><svg width="9" height="9" viewBox="0 0 10 10"><rect x="0" y="2" width="10" height="7" fill="none" stroke="var(--teal)"/><path d="M0 2l5 4 5-4" fill="none" stroke="var(--teal)"/></svg>sales@nimbrix.com</p>
    <p class="contact"><svg width="9" height="9" viewBox="0 0 10 10"><path d="M2 0l2 2-1 2 3 3 2-1 2 2-2 2C4 10 0 6 0 2z" fill="var(--teal)"/></svg>1-833-Nimbrix<br>555-014-2290</p>
    <p class="contact"><svg width="9" height="9" viewBox="0 0 10 10"><circle cx="5" cy="5" r="4.3" fill="none" stroke="var(--teal)"/><path d="M5 2v3h2" fill="none" stroke="var(--teal)"/></svg>Mon-Fri: 8:30 AM - 5 PM EST</p>
    <p class="open">OPEN <span>24X7</span> <small>FOR SERVICE IMPACTING ISSUES</small></p>
  </section>
  <div class="rule" style="left:340px;top:700px;width:210px"></div>

  <div class="brand"><i></i>NIMBRIX</div>

  <section class="headline">
    <p class="light">REDEFINING</p>
    <p class="big">CLOUD</p>
    <p class="mid">COMMUNICATION</p>
    <div class="bar"></div>
    <p class="tagline">Work from the <b>OFFICE, HOME</b><br>or on the road.</p>
  </section>

  <p class="web right-web"><svg width="11" height="11" viewBox="0 0 12 12"><circle cx="6" cy="6" r="5" fill="none" stroke="var(--teal)" stroke-width="1.2"/><path d="M1 6h10M6 1c2 2 2 8 0 10M6 1c-2 2-2 8 0 10" fill="none" stroke="var(--teal)"/></svg>www.<b>nimbrix</b>.com</p>
  <div class="rule" style="left:760px;top:696px;width:320px"></div>
</div>
</body>
</html>
```